Business Card for Jewelry Business

We need a new namecard design for a jewelry company based in Bangkok, Thailand. We have a new website recently and want the new namecard to reflect our new modern image. I have uploaded our old namecard to show you the information that needs to be on the namecard. Pls check our website www.qelnotrax.com for the new color scheme to help design the new namecard.

```html
<!DOCTYPE html>
<html lang="en">
<head>
<meta charset="utf-8">
<title>Qelnotrax Jewelry – Business Card</title>
<link href="https://fonts.googleapis.com/css2?family=Cormorant+Garamond:wght@500;600&family=Poppins:wght@400;500&display=swap" rel="stylesheet">
<style>
  :root {
    --bg: #b9b9b9;
    --ink: #222222;
    --paper: #ffffff;
    --teal: #52c4cc;
    --muted: #d9d4cc;
    --serif: "Cormorant Garamond", "Times New Roman", serif;
    --sans: "Poppins", Arial, sans-serif;
  }
  html, body { margin: 0; padding: 0; overflow: hidden; }
  body {
    width: 1200px; height: 788px;
    background: var(--bg);
    position: relative;
  }
  .card {
    position: absolute;
    width: 560px; height: 320px;
    border-radius: 22px;
    overflow: hidden;
    box-shadow: 0 10px 24px rgba(0,0,0,.25);
  }
  .card--front { left: 40px; top: 70px; background: var(--paper); }
  .card--back { left: 600px; top: 398px; background: var(--ink); }

  .front-shapes { position: absolute; inset: 0; }

  .holder { position: absolute; left: 30px; top: 56px; }
  .holder__name {
    font-family: var(--serif); font-weight: 600;
    color: var(--teal); font-size: 30px; letter-spacing: 1.5px;
    margin: 0; line-height: 1;
  }
  .holder__title {
    font-family: var(--sans); font-size: 12px; color: var(--ink);
    margin: 4px 0 0;
  }

  .wordmark {
    position: absolute; right: 130px; top: 22px;
    text-align: right; font-family: var(--serif); font-weight: 500;
    color: var(--ink); line-height: 1;
  }
  .wordmark__name { font-size: 38px; letter-spacing: 1px; display: block; }
  .wordmark__sub { font-size: 13px; letter-spacing: 2px; display: block; margin-top: 4px; }

  .badge {
    position: absolute; left: 398px; top: 120px;
    width: 136px; height: 136px; border-radius: 50%;
    background: var(--paper);
  }
  .badge::after {
    content: ""; position: absolute; inset: 8px;
    border-radius: 50%; border: 2px solid var(--muted);
  }

  .contacts {
    position: absolute; left: 30px; top: 150px; width: 370px;
    font-family: var(--sans); color: var(--paper);
    font-size: 10.5px; line-height: 1.55;
  }
  .contacts__row { display: flex; gap: 14px; white-space: nowrap; }
  .contacts__item { display: inline-flex; align-items: center; gap: 5px; }
  .icon { width: 10px; height: 10px; fill: var(--teal); flex: none; }
  .address { margin: 8px 0 0; font-style: normal; }

  .back-mark {
    position: absolute; right: 40px; top: 110px; text-align: right;
    font-family: var(--serif); font-weight: 500; color: var(--paper); line-height: 1;
  }
  .back-mark__name { font-size: 54px; letter-spacing: 1.5px; display: block; }
  .back-mark__sub { font-size: 17px; letter-spacing: 3px; display: block; margin-top: 8px; }
</style>
</head>
<body>

<section class="card card--front" aria-label="Business card front">
  <svg class="front-shapes" viewBox="0 0 560 320" width="560" height="320" aria-hidden="true">
    <polygon points="430,110 560,40 560,240 500,240" fill="var(--teal)"/>
    <rect x="0" y="138" width="560" height="150" fill="var(--ink)"/>
    <polygon points="430,110 560,40 560,138 430,138" fill="var(--teal)"/>
  </svg>

  <div class="holder">
    <h1 class="holder__name">NARA VELINDO</h1>
    <p class="holder__title">Sales &amp; Product Development Manager</p>
  </div>

  <div class="wordmark">
    <span class="wordmark__name">QELNOTRAX</span>
    <span class="wordmark__sub">JEWELRY</span>
  </div>

  <div class="badge" aria-hidden="true"></div>

  <div class="contacts">
    <div class="contacts__row">
      <span class="contacts__item"><svg class="icon" viewBox="0 0 10 10"><path d="M2 0.5 L3.8 2.6 L3 3.8 Q4 6 6.2 7 L7.4 6.2 L9.5 8 L8.4 9.5 Q1 8.5 0.5 1.6 Z"/></svg>+662-555-0142-3</span>
      <span class="contacts__item"><svg class="icon" viewBox="0 0 10 10"><rect x="2.5" y="0.5" width="5" height="3"/><rect x="0.5" y="3.5" width="9" height="4" rx="1"/><rect x="2.5" y="7" width="5" height="2.5"/></svg>+662-555-0187</span>
      <span class="contacts__item"><svg class="icon" viewBox="0 0 10 10"><rect x="0.5" y="2" width="9" height="6.5"/><path d="M0.5 2 L5 6 L9.5 2" stroke="var(--ink)" fill="none"/></svg>nara@qelnotrax.com</span>
    </div>
    <div class="contacts__row">
      <span class="contacts__item"><svg class="icon" viewBox="0 0 10 10"><rect x="0.5" y="2" width="9" height="6.5"/><path d="M0.5 2 L5 6 L9.5 2" stroke="var(--ink)" fill="none"/></svg>info@qelnotrax.com</span>
      <span class="contacts__item"><svg class="icon" viewBox="0 0 10 10"><circle cx="5" cy="5" r="4.5"/><path d="M0.5 5 H9.5 M5 0.5 Q2 5 5 9.5 Q8 5 5 0.5" stroke="var(--ink)" stroke-width="0.8" fill="none"/></svg>www.qelnotrax.com</span>
    </div>
    <div class="contacts__row">
      <span class="contacts__item"><svg class="icon" viewBox="0 0 10 10"><circle cx="5" cy="5" r="4.5"/></svg>Qelnotrax Jewelry</span>
      <span class="contacts__item"><svg class="icon" viewBox="0 0 10 10"><rect x="0.5" y="0.5" width="9" height="9" rx="2.5"/></svg>QelnotraxJwl</span>
    </div>
    <address class="address">
      Qelnotrax Jewelry Co.,Ltd.<br>
      48 Moo 7 Sukhaprom Road, Trade Zone 2,<br>
      Bang Phli Craft Estate, Bang Phli,<br>
      Bangkok 10540 Thailand
    </address>
  </div>
</section>

<section class="card card--back" aria-label="Business card back">
  <div class="back-mark">
    <span class="back-mark__name">QELNOTRAX</span>
    <span class="back-mark__sub">JEWELRY</span>
  </div>
</section>

</body>
</html>
```